Face book & Instagram ad needed

I am in need of a simple static image ad to be used for Facebook & Instagram. A photo of a nice roof on a nice house. "Instant Satellite Roof Estimates" "Your house, your time & instant estimate" . Our logo file is here: https://www.filvorra.example/scl/fo/q37tmw5ze81kpdaxnrb0z/KTbWP9GMLnhVc4XeqsFTa2w?rlkey=zx7ve2kam4ndpt63bqyjr5w4c&dl=0

Multiple variations will be purchased.

```html
<!DOCTYPE html>
<html lang="en">
<head>
<meta charset="utf-8">
<title>Instant Satellite Roof Estimates – Crestline Roofing</title>
<link href="https://fonts.googleapis.com/css2?family=Kanit:ital,wght@0,500;0,600;1,600;1,800&display=swap" rel="stylesheet">
<style>
  :root {
    --sky-top: #3d7cc0;
    --sky-mid: #86aed6;
    --sky-low: #c7d6e4;
    --house-top: #3a4047;
    --house-low: #23282d;
    --lawn: #3b7a25;
    --lawn-deep: #1c3f10;
    --white: #ffffff;
    --ink: #0a0a0a;
    --cyan-a: #0fb6f0;
    --cyan-b: #5fd8ff;
  }
  * { margin: 0; padding: 0; box-sizing: border-box; }
  html, body { width: 1200px; height: 1200px; overflow: hidden; background: #ffffff; }
  .ad {
    position: relative;
    width: 1200px;
    height: 1200px;
    overflow: hidden;
    font-family: "Kanit", "Arial", sans-serif;
    color: var(--white);
  }
  .ad__sky {
    position: absolute;
    left: 0; right: 0; top: 0;
    height: 780px;
    background: linear-gradient(180deg, var(--sky-top) 0%, var(--sky-mid) 35%, var(--sky-low) 70%);
  }
  .ad__lawn {
    position: absolute;
    left: 0; right: 0; top: 760px; bottom: 0;
    background: linear-gradient(180deg, var(--lawn) 0%, #2f6a1c 45%, var(--lawn-deep) 100%);
  }
  .ad__house {
    position: absolute;
    left: 22px;
    right: 0;
    top: 355px;
    height: 440px;
    background: linear-gradient(180deg, var(--house-top) 0%, var(--house-low) 100%);
    border-top: 3px solid var(--cyan-b);
    border-bottom: 3px solid var(--cyan-b);
  }
  .ad__shade {
    position: absolute;
    left: 0; right: 0; bottom: 0;
    height: 440px;
    background: linear-gradient(180deg, rgba(0,0,0,0) 0%, rgba(0,0,0,0.3) 60%, rgba(0,0,0,0.45) 100%);
  }
  .headline {
    position: absolute;
    top: 50px;
    left: 0; right: 0;
    text-align: center;
    font-weight: 800;
    font-style: italic;
    font-size: 114px;
    line-height: 1.1;
    letter-spacing: 3px;
    text-shadow: 0 4px 10px rgba(0,0,0,0.25);
  }
  .banner {
    position: absolute;
    top: 194px;
    left: 250px;
    width: 700px;
    height: 93px;
  }
  .banner svg { position: absolute; inset: 0; }
  .banner__text {
    position: relative;
    display: block;
    text-align: center;
    font-weight: 800;
    font-style: italic;
    font-size: 76px;
    line-height: 93px;
    color: var(--ink);
    letter-spacing: 3px;
  }
  .tagline {
    position: absolute;
    top: 782px;
    left: 0; right: 0;
    text-align: center;
    font-weight: 600;
    font-style: italic;
    font-size: 82px;
    line-height: 1.08;
    letter-spacing: 1px;
    text-shadow: 0 3px 10px rgba(0,0,0,0.45);
  }
  .benefits {
    position: absolute;
    left: 40px;
    top: 1005px;
    list-style: none;
    font-weight: 500;
    font-size: 29px;
    line-height: 52px;
  }
  .benefits li::before {
    content: "";
    display: inline-block;
    width: 10px; height: 10px;
    border-radius: 50%;
    background: var(--white);
    margin-right: 12px;
    vertical-align: middle;
  }
  .brand {
    position: absolute;
    right: 24px;
    bottom: 40px;
    width: 300px;
    text-align: center;
    font-weight: 600;
    color: var(--white);
    line-height: 1;
  }
  .brand__name { display: block; font-size: 56px; letter-spacing: 2px; }
  .brand__sub { display: block; font-size: 30px; letter-spacing: 8px; margin-top: 10px; }
</style>
</head>
<body>
  <main class="ad">
    <div class="ad__sky"></div>
    <div class="ad__lawn"></div>
    <div class="ad__house" role="img" aria-label="Photograph of a large dark-shingled house with glowing blue roof-line outlines, chimneys, white-framed windows and a stone patio"></div>
    <div class="ad__shade"></div>

    <h1 class="headline">INSTANT SATELLITE</h1>

    <div class="banner">
      <svg width="700" height="93" viewBox="0 0 700 93" aria-hidden="true">
        <defs>
          <linearGradient id="bannerFill" x1="0" y1="0" x2="1" y2="0">
            <stop offset="0" stop-color="#0fb6f0"/>
            <stop offset="1" stop-color="#5fd8ff"/>
          </linearGradient>
        </defs>
        <polygon points="10,0 700,0 690,93 0,93" fill="url(#bannerFill)"/>
      </svg>
      <span class="banner__text">ROOF ESTIMATES</span>
    </div>

    <p class="tagline">Your House, Your Time<br>&amp; Instant Estimate</p>

    <ul class="benefits">
      <li>Accurate Roof Measurements</li>
      <li>Fast Online Quotes</li>
      <li>Save Time &amp; Money</li>
    </ul>

    <div class="brand">
      <span class="brand__name">CRESTLINE</span>
      <span class="brand__sub">ROOFING</span>
    </div>
  </main>
</body>
</html>
```